Our website, is loosely based on a grant proposal submitted to the Northern Vascular Society last year for a community-based project that could improve the health of the community at large, I have attached this file for your review (underline "loosely). The idea is to create a "patient navigator" a website where patients can both learn and use as a resource for their care. I have been working on the project for some time, but my other responsibilities as a cardiologist have not allowed me time to learn and design a website of this type. Our website is intended for a spanish speaking audience and is in Spanish language. Designs in english will have to be translated. Our name: AcademiaBrisa.com: means a health university: One option is to have the website have a "university" theme. The project calls for: An initial: easy registration process: collecting name, DOB and city. Simplicity is key, many of our patients barely use computers, and this site is meant to make things easier, not complicate them. The web site should work as an extension of the doctors office, so it should be serious, creative, addictive, engaging. Doctors will see the patients in the office then refer them to the website to continue their learning about their conditions. There should be a page where patients can post questions: a panel of doctors: represented with their pictures, (in circles? around the question answered?) titles and small resumes (our "faculty") answers them. Every person that will attach themself to this website will have a title: doctors and nurses will be professors, residents and fellows will be assistant professors, aids can be PA?. The site should have a market place where people can purchase items that doctors recommend including foods, products and devices; here too, we can have a "bookshop". This should have a flexible mechanism for doctors to add their recommendations a patients can have access to them. Very important: there should be a site intended to be a classroom, this is the meat of this protect: where people can watch videos our staff will make to learn about different subjects; the site should keep track of the videos watched by the person and eventually "graduate them". These videos will be created by my staff, and added over time to the site, students should be able to "request" classes (videos). It should have a site where people can input their medications (notebook), have them stored and printed as a list if necessary. And finally it should have a contact and references section. We have set up a relationship with another site that help people count calories: and a link to this should be available. We have a link to our twitter account, This protect is intended to expand, and we hope to establish a long term relationship with the design team to expand it as needed in the future. The site is on PageHarbor and can be seen in its current form at AcademiaBrisa.com . We have had a logo designed with specific colors of the hospital I work with and one plan is to present it to our hospital to adopt our page in it final form. Again, this site is in spanish and intended for a spanish audience.

Target Market(s)

Spanish speaking, late 30s to early 60s audience.

Industry/Entity Type

Community

Number of Pages Required

Font styles to use
Sans Serif

Colors
a64599
fceff5
3277b5

Requirements
Must have
• A simple, accesible look
Nice to have
• Animations, moving parts
Should not have
• English

```html
<!DOCTYPE html>
<html lang="es">
<head>
<meta charset="utf-8">
<title>AcademiaBrisa</title>
<link href="https://fonts.googleapis.com/css2?family=Open+Sans:wght@300;400;600&display=swap" rel="stylesheet">
<style>
:root{
  --purple:#a64599;
  --blush:#fceff5;
  --blue:#3277b5;
  --navy:#2a5183;
  --ink:#2c4a72;
  --text:#555b63;
  --orange:#f7941d;
  --line:#dcdcdc;
  --white:#ffffff;
}
*{margin:0;padding:0;box-sizing:border-box}
html,body{width:1200px;height:2173px;overflow:hidden;background:var(--white)}
body{font-family:"Open Sans",Arial,sans-serif;color:var(--text);position:relative}
.abs{position:absolute}

/* Hero */
.hero{position:absolute;left:0;top:0;width:1200px;height:594px;overflow:hidden}
.hero-photo{position:absolute;inset:0;background:linear-gradient(100deg,#8e9fb4 0%,#c9ced3 45%,#e9e6e0 62%,#f4f1ec 80%,#dcd7cf 100%)}
.hero-panel{position:absolute;left:0;top:0}
.logo{left:82px;top:30px;font-size:38px;font-weight:300;color:var(--white);letter-spacing:-.5px}
.nav{position:absolute;left:0;top:47px;width:1200px;height:24px;font-size:15px;color:var(--white)}
.nav span{position:absolute;top:0;white-space:nowrap}
.hero-title{left:82px;top:136px;font-size:52px;line-height:57px;font-weight:300;color:var(--white)}
.hero-text{left:82px;top:259px;width:440px;font-size:16.5px;line-height:20px;color:var(--white)}
.hero-buttons{left:86px;top:346px;width:411px;height:44px;border:1.5px solid rgba(255,255,255,.75);border-radius:8px;display:flex}
.hero-buttons span{flex:1;display:flex;align-items:center;justify-content:center;color:var(--white);font-size:17px;border-left:1.5px solid rgba(255,255,255,.75)}
.hero-buttons span:first-child{border-left:none}
.quick{color:var(--white);font-size:15px;display:flex;align-items:center;gap:22px}
.quick svg{width:40px;height:34px}

/* Intro */
.intro-title{left:0;width:1200px;top:662px;text-align:center;font-size:31px;font-weight:300;color:var(--ink)}
.intro-text{left:105px;width:990px;top:719px;text-align:center;font-size:14.5px;line-height:32px;color:var(--text)}
.promo{left:115px;top:843px;width:970px;height:215px;background:linear-gradient(180deg,#3d3a34 0%,#4e4a43 45%,#2b2824 100%)}
.promo-label{left:115px;top:843px;width:970px;height:215px;display:flex;align-items:center;justify-content:center;gap:14px;color:var(--white);font-size:38px;font-weight:400}
.play{width:82px;height:82px}

/* Features */
.divider-v{left:599px;top:1106px;width:1px;height:255px;background:var(--line)}
.divider-h{left:115px;top:1233px;width:970px;height:1px;background:var(--line)}
.feature{width:440px}
.feature svg{position:absolute;left:0;top:0;width:66px;height:66px}
.feature h3{position:absolute;left:99px;top:-3px;font-size:21px;font-weight:400;color:#333;white-space:nowrap}
.feature p{position:absolute;left:99px;top:28px;width:335px;font-size:12.5px;line-height:16px;letter-spacing:-.2px;color:#666}

/* Video tiles */
.tile{top:1419px;width:532px;height:286px}
.tile-one{left:66px;background:linear-gradient(90deg,#3a2a1e 0%,#6b4b33 35%,#d9cfc4 55%,#4a3323 100%)}
.tile-two{left:602px;background:linear-gradient(180deg,#2b2620 0%,#5a4d40 50%,#6e5338 100%)}
.tile-label{top:1419px;width:532px;height:286px;display:flex;flex-direction:column;align-items:center;justify-content:center;color:var(--white);font-size:22px}
.tile-label svg{width:82px;height:82px;margin-bottom:12px;margin-top:20px}

/* Vision */
.vision{left:0;top:1776px;width:1200px;height:397px;background:var(--purple)}
.vision-title{left:0;width:1200px;top:1826px;text-align:center;color:var(--white);font-size:33px;font-weight:300}
.goal{top:1898px;width:260px;text-align:center;color:var(--white)}
.goal-art{width:124px;height:124px;margin:0 auto;border-radius:12px}
.art-idea{background:#4fc94a}
.art-world{background:#3ac4e0}
.art-screen{background:#5e6a7c}
.art-award{background:#f7b52a}
.goal h4{margin-top:28px;font-size:22px;font-weight:400}
.goal p{margin-top:6px;font-size:13px;line-height:23px}
</style>
</head>
<body>

<section class="hero">
  <div class="hero-photo" role="img" aria-label="Fotografía de un médico sonriente con bata blanca y estetoscopio"></div>
  <svg class="hero-panel" width="600" height="594" viewBox="0 0 600 594" aria-hidden="true">
    <path d="M0 0 H592 C548 180 536 400 551 594 H0 Z" fill="var(--navy)" fill-opacity=".93"/>
  </svg>
  <div class="abs logo">AcademiaBrisa</div>
  <nav class="nav">
    <span style="left:653px">Sobre nosotros</span>
    <span style="left:795px">Servicios</span>
    <span style="left:892px">Carrera</span>
    <span style="left:974px">Contacto</span>
    <svg style="position:absolute;left:1080px;top:2px" width="32" height="18" viewBox="0 0 32 18" aria-label="Idioma">
      <circle cx="8" cy="9" r="7.5" fill="var(--white)"/>
      <path d="M21 7 h8 l-4 5 z" fill="var(--white)"/>
    </svg>
  </nav>
  <h1 class="abs hero-title">Bienvenidos a<br>Academia Brisa!</h1>
  <p class="abs hero-text">Nuestra nueva pagina esta dedicada a tu salud. Tu! que hablas español y vives aquí en los Estados Unidos!, esta pagina esta diseñada contigo en mente.</p>
  <div class="abs hero-buttons"><span>Iniciar sesión</span><span>Registro</span><span>Cuenta</span></div>

  <div class="abs quick" style="left:94px;top:427px">
    <svg viewBox="0 0 40 34" aria-hidden="true"><rect x="3" y="4" width="34" height="22" fill="none" stroke="#fff" stroke-width="2"/><circle cx="11" cy="14" r="3" fill="#fff"/><path d="M7 26 v-6 h9 l8 -5" stroke="#fff" stroke-width="2" fill="none"/><path d="M1 30 h38" stroke="#fff" stroke-width="2"/></svg>Clases
  </div>
  <div class="abs quick" style="left:309px;top:427px">
    <svg viewBox="0 0 40 34" aria-hidden="true"><rect x="10" y="2" width="20" height="30" rx="2" fill="none" stroke="#fff" stroke-width="2"/><rect x="13" y="5" width="14" height="6" fill="#fff"/><g fill="#fff"><rect x="13" y="14" width="3" height="3"/><rect x="18.5" y="14" width="3" height="3"/><rect x="24" y="14" width="3" height="3"/><rect x="13" y="20" width="3" height="3"/><rect x="18.5" y="20" width="3" height="3"/><rect x="24" y="20" width="3" height="3"/><rect x="13" y="26" width="3" height="3"/><rect x="18.5" y="26" width="3" height="3"/><rect x="24" y="26" width="3" height="3"/></g></svg>Calculadora
  </div>
  <div class="abs quick" style="left:94px;top:487px">
    <svg viewBox="0 0 40 34" aria-hidden="true"><path d="M20 7 C14 3 7 3 3 5 V30 C7 28 14 28 20 32 C26 28 33 28 37 30 V5 C33 3 26 3 20 7 Z M20 7 V32" fill="none" stroke="#fff" stroke-width="2"/></svg>Libreria
  </div>
  <div class="abs quick" style="left:309px;top:487px">
    <svg viewBox="0 0 40 34" aria-hidden="true"><path d="M6 5 h5 l4 17 h16 l3 -12 h-20" fill="none" stroke="#fff" stroke-width="2"/><circle cx="17" cy="28" r="2.5" fill="#fff"/><circle cx="28" cy="28" r="2.5" fill="#fff"/></svg>Mercado
  </div>
</section>

<h2 class="abs intro-title">Lorem ipsum dolor sit amet, consectetur adipiscing elit</h2>
<p class="abs intro-text">Lorem ipsum dolor sit amet, consectetur adipiscing elit, sed do eiusmod tempor incididunt ut labore et dolore magna aliqua. Ut enim ad minim veniam, quis nostrud exercitation ullamco laboris nisi ut aliquip ex ea commodo consequat. Duis aute irure dolor in reprehenderit in voluptate velit esse cillum dolore eu fugiat nulla pariatur. Excepteur sint occaecat cupidatat non proident.</p>

<div class="abs promo" role="img" aria-label="Fotografía de un auditorio lleno de estudiantes durante una clase"></div>
<div class="abs promo-label">
  <span>Vea nuestro</span>
  <svg class="play" viewBox="0 0 82 82" aria-hidden="true"><circle cx="41" cy="41" r="38" fill="rgba(255,255,255,.12)" stroke="#fff" stroke-width="3"/><path d="M33 26 L58 41 L33 56 Z" fill="#fff"/></svg>
  <span>Promocional Vídeo</span>
</div>

<div class="abs divider-v"></div>
<div class="abs divider-h"></div>

<div class="abs feature" style="left:120px;top:1114px">
  <svg viewBox="0 0 66 66" aria-hidden="true"><circle cx="33" cy="37" r="24" fill="none" stroke="var(--orange)" stroke-width="6"/><rect x="28" y="3" width="10" height="6" fill="var(--orange)"/><rect x="31" y="8" width="4" height="6" fill="var(--orange)"/><path d="M33 37 L22 26" stroke="var(--orange)" stroke-width="5" stroke-linecap="round"/><path d="M52 12 l5 5" stroke="var(--orange)" stroke-width="5" stroke-linecap="round"/></svg>
  <h3>Ahorre tiempo y esfuerzo</h3>
  <p>Velit enim nisi pulvinar, sociis rhoncus tincidunt platea auctor tincidunt nisi ut. Odio integer in, dolor, turpis ultrices est, aliquam. Parturient sociis, placera</p>
</div>
<div class="abs feature" style="left:665px;top:1114px">
  <svg viewBox="0 0 66 66" aria-hidden="true"><path d="M30 3 C14 3 5 15 6 28 L2 38 L8 40 V50 C8 54 12 55 18 54 V64 H46 V48 C56 42 60 32 58 22 C55 10 44 3 30 3 Z" fill="var(--orange)"/><circle cx="33" cy="26" r="11" fill="none" stroke="#fff" stroke-width="4" stroke-dasharray="4 3"/><circle cx="33" cy="26" r="5" fill="#fff"/></svg>
  <h3>Técnicas avanzadas</h3>
  <p>Velit enim nisi pulvinar, sociis rhoncus tincidunt platea auctor tincidunt nisi ut. Odio integer in, dolor, turpis ultrices est, aliquam. Parturient sociis, placera</p>
</div>
<div class="abs feature" style="left:120px;top:1254px">
  <svg viewBox="0 0 66 66" aria-hidden="true"><rect x="3" y="6" width="46" height="34" rx="2" fill="none" stroke="var(--orange)" stroke-width="4"/><path d="M20 40 v10 h-6 M32 40 v10 h6" stroke="var(--orange)" stroke-width="4" fill="none"/><rect x="44" y="26" width="19" height="34" rx="3" fill="#fff" stroke="var(--orange)" stroke-width="4"/><circle cx="53.5" cy="54" r="2" fill="var(--orange)"/></svg>
  <h3>Acceso a todas partes</h3>
  <p>Velit enim nisi pulvinar, sociis rhoncus tincidunt platea auctor tincidunt nisi ut. Odio integer in, dolor, turpis ultrices est, aliquam. Parturient sociis, placera</p>
</div>
<div class="abs feature" style="left:665px;top:1254px">
  <svg viewBox="0 0 66 66" aria-hidden="true"><g fill="none" stroke="var(--orange)" stroke-width="4" stroke-linecap="round"><path d="M31 8 C24 2 12 5 12 14 C4 16 3 26 8 31 C2 37 6 48 14 48 C15 57 26 61 31 55 Z"/><path d="M35 8 C42 2 54 5 54 14 C62 16 63 26 58 31 C64 37 60 48 52 48 C51 57 40 61 35 55 Z"/><path d="M18 22 q6 2 8 8 M16 38 q6 -2 10 2 M48 22 q-6 2 -8 8 M50 38 q-6 -2 -10 2"/></g></svg>
  <h3>Aumente su conocimiento</h3>
  <p>Velit enim nisi pulvinar, sociis rhoncus tincidunt platea auctor tincidunt nisi ut. Odio integer in, dolor, turpis ultrices est, aliquam. Parturient sociis, placera</p>
</div>

<div class="abs tile tile-one" role="img" aria-label="Fotografía de una doctora hablando frente a una biblioteca"></div>
<div class="abs tile-label" style="left:66px">
  <svg viewBox="0 0 82 82" aria-hidden="true"><circle cx="41" cy="41" r="38" fill="rgba(255,255,255,.12)" stroke="#fff" stroke-width="3"/><path d="M33 26 L58 41 L33 56 Z" fill="#fff"/></svg>
  <span>¿Qué es Academia Brisa!</span>
</div>
<div class="abs tile tile-two" role="img" aria-label="Fotografía de una computadora portátil abierta sobre una mesa de madera"></div>
<div class="abs tile-label" style="left:602px">
  <svg viewBox="0 0 82 82" aria-hidden="true"><circle cx="41" cy="41" r="38" fill="rgba(255,255,255,.12)" stroke="#fff" stroke-width="3"/><path d="M33 26 L58 41 L33 56 Z" fill="#fff"/></svg>
  <span>Ver los cursos</span>
</div>

<section class="abs vision"></section>
<h2 class="abs vision-title">Visión y Objetivo</h2>

<div class="abs goal" style="left:61px">
  <div class="goal-art art-idea" role="img" aria-label="Ilustración de una bombilla encendida"></div>
  <h4>Loren Ipsum Dolor</h4>
  <p>Elementum tristique aenean elit?<br>Aliquam lundium ac magnis augue</p>
</div>
<div class="abs goal" style="left:337px">
  <div class="goal-art art-world" role="img" aria-label="Ilustración del planeta Tierra"></div>
  <h4>Loren Ipsum Dolor</h4>
  <p>Elementum tristique aenean elit?<br>Aliquam lundium ac magnis augue</p>
</div>
<div class="abs goal" style="left:610px">
  <div class="goal-art art-screen" role="img" aria-label="Ilustración de una computadora portátil con contenidos de cursos"></div>
  <h4>Loren Ipsum Dolor</h4>
  <p>Elementum tristique aenean elit?<br>Aliquam lundium ac magnis augue</p>
</div>
<div class="abs goal" style="left:883px">
  <div class="goal-art art-award" role="img" aria-label="Ilustración de una medalla de primer lugar"></div>
  <h4>Loren Ipsum Dolor</h4>
  <p>Elementum tristique aenean elit?<br>Aliquam lundium ac magnis augue</p>
</div>

</body>
</html>
```